New Stationary for our business

We are a gift business and would like to create a new corporate image with new stationary and design.

We would like a Classic Corporate look with a touch of Flair.

We would need:
Envelopes
Letter Head
Business Cards
With Comp Slips
Note Pads
Etc...

Our details are:

Basket Haven Pty Ltd
518 Pelling Street, Carrow Vale, Victoria, 3071
1800 742 918
www.baskethaven.com.au
sales@baskethaven.com.au

ABN: 62 804 319 775

Target Market(s)

Corporate Look

Industry/Entity Type

Marketing

Contact Information for Business Card

Basket Haven Pty Ltd
1800 742 918
518 Pelling Street
Carrow Vale 3071
Victoria Australia

Darren Pelloni - Managing Director
darren.pelloni@baskethaven.com.au
0417 586 902

Logo Text

Basket Haven - The Present Experts

Colors

Designer to choose colors to be used in the design.

Requirements
Must have
• Look and Feel upmarket and exclusive

```html
<!DOCTYPE html>
<html lang="en">
<head>
<meta charset="utf-8">
<title>Basket Haven – Stationery Set</title>
<link rel="stylesheet" href="https://fonts.googleapis.com/css2?family=Cormorant+Garamond:wght@500&family=Lato:wght@400;700&family=Michroma&display=swap">
<style>
:root{
  --teal:#1b9bb6;
  --teal-dark:#17879f;
  --ink:#474747;
  --ink-soft:#6b6b6b;
  --paper:#ffffff;
  --paper-tint:#f3f6f8;
  --stage:#d1c4ab;
  --flap:#474747;
}
*{box-sizing:border-box;margin:0;padding:0}
html,body{width:1200px;height:1200px;overflow:hidden;background:var(--stage)}
body{position:relative;font-family:"Lato",sans-serif;color:var(--ink)}
.piece{position:absolute;background:var(--paper)}

/* brand lockup */
.brand{position:absolute;text-align:center;font-family:"Cormorant Garamond",serif;color:var(--teal);font-size:var(--s);line-height:1}
.brand .dot{width:1.5em;height:1.5em;border-radius:50%;background:currentColor;margin:0 auto .35em}
.brand .rule{height:1px;background:var(--ink);width:5.4em;margin:0 auto .28em}
.brand .name{font-weight:500;letter-spacing:.03em;white-space:nowrap}
.brand .tag{font-size:max(5.5px,.4em);color:var(--ink);letter-spacing:.04em;margin-top:.3em;white-space:nowrap}
.brand .abn{font-family:"Lato",sans-serif;font-size:max(5px,.3em);color:var(--ink);margin-top:.35em;white-space:nowrap}
.brand.on-teal{color:#fff}
.brand.on-teal .rule{background:#fff}
.brand.on-teal .tag,.brand.on-teal .abn{color:#fff}

.hero{left:0;width:1200px;top:60px;--s:46px}
.hero .dot{width:1.9em;height:1.9em;margin-bottom:.55em}
.hero .rule{width:5.2em;height:2px;margin-bottom:.4em}
.hero .abn{font-size:.32em;margin-top:.55em}

.contact{font-size:6px;line-height:1.4;color:var(--ink)}

/* folder */
.folder-flaps{position:absolute;left:114px;top:346px}
.folder-cover{left:158px;top:346px;width:228px;height:312px;background:var(--teal)}
.folder-cover .watermark{position:absolute;left:10px;top:30px;width:208px;height:200px;border-radius:50%;background:radial-gradient(circle,rgba(255,255,255,.12),rgba(255,255,255,0) 70%)}
.folder-icons{position:absolute;left:6px;right:6px;bottom:12px;display:flex;justify-content:space-between;color:#fff;font-size:5px;line-height:1.3;text-align:center}
.folder-icons .ico{width:10px;height:10px;margin:0 auto 4px;background:var(--flap);transform:rotate(45deg);display:flex;align-items:center;justify-content:center}
.folder-icons svg{transform:rotate(-45deg)}
.folder-inside{left:386px;top:346px;width:228px;height:312px}
.folder-inside .brand{left:0;right:0;top:118px;--s:15px}
.folder-inside .web{position:absolute;left:0;right:0;bottom:18px;text-align:center;font-size:6px}

/* letterhead */
.letterhead{left:658px;top:346px;width:218px;height:308px;border-top:3px solid var(--teal)}
.letterhead .brand{left:22px;top:26px;--s:8px}
.letterhead .contact{position:absolute;right:22px;top:28px;text-align:right;font-size:5px}
.letterhead .meta{position:absolute;left:26px;right:22px;top:80px;display:flex;justify-content:space-between;font-size:5.5px;font-weight:700}
.letterhead .meta small{display:block;font-weight:400;font-size:5px}
.letterhead .body{position:absolute;left:26px;right:22px;top:108px;font-size:5px;line-height:1.35}
.letterhead .body p{margin-bottom:5px}
.letterhead .sign{position:absolute;right:22px;top:248px;font-size:5.5px;font-weight:700;text-align:left}
.letterhead .sign small{display:block;font-weight:400;font-size:5px}
.letterhead .sign i{display:block;width:34px;border-bottom:1px solid var(--ink-soft);height:10px}
.letterhead .foot{position:absolute;left:0;right:0;bottom:8px}

/* business cards */
.card-front{left:872px;top:379px;width:202px;height:115px;background:var(--teal)}
.card-front .brand{left:0;width:116px;top:28px;--s:10px}
.card-front .divider{position:absolute;left:116px;top:0;bottom:0;width:1px;background:rgba(255,255,255,.8)}
.card-front .lines{position:absolute;left:121px;top:42px;color:#fff;font-size:5.5px;line-height:1.4;list-style:none}
.card-front .lines li{display:flex;gap:4px;margin-bottom:2px}
.card-front .lines li::before{content:"";width:3px;height:3px;margin-top:2px;border:1px solid #fff;transform:rotate(45deg);flex:none}
.card-back{left:872px;top:519px;width:202px;height:115px;background:var(--paper-tint)}
.card-back .brand{left:0;right:0;top:26px;--s:10px}
.card-back .web{position:absolute;left:0;right:0;bottom:9px;text-align:center;font-size:5.5px}

/* envelopes */
.env-flap{left:660px;top:688px;width:251px;height:126px}
.env-flap .band{position:absolute;left:0;right:0;top:0;height:42px;background:var(--teal);border-radius:0 0 6px 6px}
.env-flap .brand{left:0;right:0;top:15px;--s:11px}
.env-window{left:839px;top:747px;width:253px;height:126px;box-shadow:0 0 0 1px rgba(0,0,0,.04)}
.env-window .window{position:absolute;left:19px;top:48px;width:85px;height:43px;border-radius:7px;background:linear-gradient(135deg,#39b3c9,var(--teal-dark));border:1px solid rgba(0,0,0,.15)}
.env-window .brand{right:14px;top:12px;--s:8px}
.env-window .contact{position:absolute;right:14px;top:68px;text-align:right}

.env-large{left:158px;top:776px;width:236px;height:334px}
.env-large .band{position:absolute;left:0;right:0;top:0;height:40px;background:var(--teal);border-radius:0 0 6px 6px}
.env-large .brand{left:0;right:0;top:14px;--s:11px}
.env-large .contact{position:absolute;left:24px;bottom:20px}

/* notepad */
.notepad{left:415px;top:774px;width:238px;height:336px}
.notepad .brand{left:22px;top:22px;--s:9px}

/* compliments slip */
.comp-slip{left:626px;top:931px;width:288px;height:133px;background:var(--paper-tint)}
.comp-slip .brand{left:24px;top:10px;--s:8px}
.comp-slip .contact{position:absolute;left:24px;top:58px;line-height:1.35}
.comp-slip .ribbon{position:absolute;left:0;top:106px;width:140px;height:17px;background:var(--teal);clip-path:polygon(0 0,88% 0,100% 100%,0 100%);color:#fff;font-family:"Michroma",sans-serif;font-size:6.5px;letter-spacing:.04em;display:flex;align-items:center;padding-left:22px;text-transform:uppercase;white-space:nowrap}
.comp-slip .side{position:absolute;right:0;top:0;width:24px;height:133px}
</style>
</head>
<body>

<div class="brand hero">
  <div class="dot"></div>
  <div class="rule"></div>
  <div class="name">BASKET HAVEN</div>
  <div class="tag">THE PRESENT EXPERTS</div>
  <div class="abn">ABN: 62 804 319 775</div>
</div>

<!-- presentation folder -->
<svg class="folder-flaps" width="300" height="366" viewBox="0 0 300 366">
  <polygon points="0,30 44,0 44,312 0,312" fill="var(--flap)"/>
  <polygon points="44,312 272,312 224,364 44,364" fill="var(--flap)"/>
</svg>
<div class="piece folder-cover">
  <div class="watermark" role="img" aria-label="Faint oversized brand circle decoration"></div>
  <div class="folder-icons">
    <div><div class="ico"><svg width="5" height="5" viewBox="0 0 10 10"><path d="M2 1l2 2-1 1.5a6 6 0 0 0 2.5 2.5L7 6l2 2-1.5 1.5C4 9 1 6 .5 2.5z" fill="#fff"/></svg></div>1800 742 918</div>
    <div><div class="ico"><svg width="5" height="5" viewBox="0 0 10 10"><rect x="1" y="2.5" width="8" height="5" fill="none" stroke="#fff"/><path d="M1 2.5l4 3 4-3" fill="none" stroke="#fff"/></svg></div>sales@baskethaven.com.au</div>
    <div><div class="ico"><svg width="5" height="5" viewBox="0 0 10 10"><path d="M5 9.5C2 6 2 4.5 2 4a3 3 0 0 1 6 0c0 .5 0 2-3 5.5z" fill="#fff"/></svg></div>518 Pelling Street,<br>Carrow Vale,<br>Victoria, 3071</div>
  </div>
</div>
<div class="piece folder-inside">
  <div class="brand">
    <div class="dot"></div>
    <div class="rule"></div>
    <div class="name">BASKET HAVEN</div>
    <div class="tag">THE PRESENT EXPERTS</div>
    <div class="abn">ABN: 62 804 319 775</div>
  </div>
  <div class="web">www.baskethaven.com.au</div>
</div>

<!-- letterhead -->
<div class="piece letterhead">
  <div class="brand">
    <div class="dot"></div>
    <div class="rule"></div>
    <div class="name">BASKET HAVEN</div>
    <div class="tag">THE PRESENT EXPERTS</div>
  </div>
  <div class="contact">1800 742 918<br>sales@baskethaven.com.au<br>518 Pelling Street, Carrow Vale,<br>Victoria, 3071<br>www.baskethaven.com.au</div>
  <div class="meta">
    <div>Dear, Mr.________<small>Designation</small><small>Company name</small></div>
    <div>DATE:2/1/2018</div>
  </div>
  <div class="body">
    <p>Thank you for choosing us for your corporate gifting needs. Each basket is packed by hand with local produce and delivered with care across Victoria.</p>
    <p>Thank you for choosing us for your corporate gifting needs. Each basket is packed by hand with local produce and delivered with care across Victoria.</p>
    <p>Thank you for choosing us for your corporate gifting needs. Each basket is packed by hand with local produce and delivered with care across Victoria.</p>
    <p>Thank you for choosing us for your corporate gifting needs. Each basket is packed by hand with local produce and delivered with care across Victoria.</p>
  </div>
  <div class="sign">YOUR NAME<small>Designation</small><i></i></div>
  <svg class="foot" width="218" height="8" viewBox="0 0 218 8">
    <line x1="26" y1="4" x2="192" y2="4" stroke="var(--ink)" stroke-width=".8"/>
    <g fill="var(--ink)"><rect x="100" y="1.5" width="4" height="4" transform="rotate(45 102 3.5)"/><rect x="107" y="1.5" width="4" height="4" transform="rotate(45 109 3.5)"/><rect x="114" y="1.5" width="4" height="4" transform="rotate(45 116 3.5)"/></g>
  </svg>
</div>

<!-- business card front -->
<div class="piece card-front">
  <div class="brand on-teal">
    <div class="dot"></div>
    <div class="rule"></div>
    <div class="name">BASKET HAVEN</div>
    <div class="tag">THE PRESENT EXPERTS</div>
    <div class="abn">ABN: 62 804 319 775</div>
  </div>
  <div class="divider"></div>
  <ul class="lines">
    <li>1800 742 918</li>
    <li>sales@baskethaven.com.au</li>
    <li>518 Pelling Street,<br>Carrow Vale, Victoria, 3071</li>
  </ul>
</div>

<!-- business card back -->
<div class="piece card-back">
  <div class="brand">
    <div class="dot"></div>
    <div class="rule"></div>
    <div class="name">BASKET HAVEN</div>
    <div class="tag">THE PRESENT EXPERTS</div>
    <div class="abn">ABN: 62 804 319 775</div>
  </div>
  <div class="web">www.baskethaven.com.au</div>
</div>

<!-- envelope, flap side -->
<div class="piece env-flap">
  <div class="band"></div>
  <div class="brand on-teal"><div class="name">BASKET HAVEN</div></div>
</div>

<!-- window envelope -->
<div class="piece env-window">
  <div class="window"></div>
  <div class="brand">
    <div class="dot"></div>
    <div class="rule"></div>
    <div class="name">BASKET HAVEN</div>
    <div class="tag">THE PRESENT EXPERTS</div>
  </div>
  <div class="contact">1800 742 918<br>sales@baskethaven.com.au<br>518 Pelling Street, Carrow Vale,<br>Victoria, 3071<br>www.baskethaven.com.au</div>
</div>

<!-- large envelope -->
<div class="piece env-large">
  <div class="band"></div>
  <div class="brand on-teal"><div class="name">BASKET HAVEN</div></div>
  <div class="contact">1800 742 918<br>sales@baskethaven.com.au<br>518 Pelling Street, Carrow Vale,<br>Victoria, 3071<br>www.baskethaven.com.au</div>
</div>

<!-- notepad -->
<div class="piece notepad">
  <div class="brand">
    <div class="dot"></div>
    <div class="rule"></div>
    <div class="name">BASKET HAVEN</div>
    <div class="tag">THE PRESENT EXPERTS</div>
    <div class="abn">ABN: 62 804 319 775</div>
  </div>
</div>

<!-- compliments slip -->
<div class="piece comp-slip">
  <div class="brand">
    <div class="dot"></div>
    <div class="rule"></div>
    <div class="name">BASKET HAVEN</div>
    <div class="tag">THE PRESENT EXPERTS</div>
  </div>
  <div class="contact">1800 742 918<br>sales@baskethaven.com.au<br>518 Pelling Street, Carrow Vale,<br>Victoria, 3071<br>www.baskethaven.com.au</div>
  <div class="ribbon">With compliments</div>
  <svg class="side" viewBox="0 0 24 133">
    <line x1="20" y1="0" x2="20" y2="133" stroke="var(--ink)" stroke-width="1.6"/>
    <g fill="var(--ink)">
      <rect x="7" y="44" width="10" height="10" transform="rotate(45 12 49)"/>
      <rect x="7" y="60" width="10" height="10" transform="rotate(45 12 65)"/>
      <rect x="7" y="76" width="10" height="10" transform="rotate(45 12 81)"/>
    </g>
  </svg>
</div>

</body>
</html>
```